Oven Cleaning Business owner needs business card design

Hi there,
Would like for a business card to be designed for myself, the owner of a professional oven cleaning business on the Sunshine Coast.
Would like it to look sleek, and modern-ish. Bit creative is encouraged too.
Include following:
Name/title: Corin ter Haghe, Owner
Phone number: 1300 482 916
Email: info@hearthshinecrew.com.au
Website: www.hearthshinecrew.com.au

```html
<!DOCTYPE html>
<html lang="en">
<head>
<meta charset="utf-8">
<title>Hearthshine Crew – Business Cards</title>
<link rel="stylesheet" href="https://fonts.googleapis.com/css2?family=Exo+2:wght@700&family=Roboto+Condensed:wght@400;700&display=swap">
<style>
  :root {
    --navy-deep: #141c3b;
    --navy: #1f2b55;
    --navy-light: #26356a;
    --teal: #1fc8c8;
    --white: #f4f5f7;
    --ink: #10142a;
    --backdrop: #2b2c30;
  }
  * { box-sizing: border-box; margin: 0; padding: 0; }
  html, body {
    width: 1200px; height: 874px; overflow: hidden;
    background: var(--backdrop);
  }
  .canvas {
    position: relative; width: 1200px; height: 874px;
  }
  .card {
    position: absolute; width: 600px; height: 342px;
    border-radius: 18px; overflow: hidden;
    box-shadow: 0 14px 30px rgba(0,0,0,.45);
  }
  .card--front {
    left: 300px; top: 74px;
    background: linear-gradient(120deg, var(--navy-deep), var(--navy-light));
    display: flex; align-items: center; justify-content: center;
  }
  .brand {
    display: flex; align-items: center; gap: 18px;
  }
  .brand__dot {
    width: 64px; height: 64px; border-radius: 50%;
    background: var(--teal); flex: none;
  }
  .brand__name {
    font-family: "Exo 2", sans-serif; font-weight: 700;
    font-size: 44px; line-height: 1; letter-spacing: 2px;
    color: var(--white); text-transform: uppercase;
  }
  .card--back {
    left: 300px; top: 458px; background: var(--white);
  }
  .card__shape { position: absolute; inset: 0; }
  .brand--stacked {
    position: absolute; left: 34px; top: 86px; width: 200px;
    flex-direction: column; gap: 14px;
  }
  .brand--stacked .brand__name {
    color: var(--ink); font-size: 30px; text-align: center;
  }
  .contact {
    position: absolute; left: 330px; top: 104px;
    font-family: "Roboto Condensed", sans-serif; color: var(--white);
  }
  .contact__name {
    font-weight: 700; font-size: 24px; color: var(--teal);
    text-transform: uppercase; letter-spacing: .3px;
  }
  .contact__title { font-size: 14px; margin-top: 2px; }
  .contact__list { list-style: none; margin-top: 34px; }
  .contact__item {
    display: flex; align-items: center; gap: 10px;
    font-size: 15px; margin-bottom: 8px;
  }
  .contact__item svg { width: 14px; height: 14px; flex: none; }
</style>
</head>
<body>
<main class="canvas">
  <section class="card card--front">
    <div class="brand">
      <span class="brand__dot"></span>
      <span class="brand__name">Hearthshine Crew</span>
    </div>
  </section>

  <section class="card card--back">
    <svg class="card__shape" viewBox="0 0 600 342" preserveAspectRatio="none">
      <path d="M282 0 Q262 232 142 342 L600 342 L600 0 Z" fill="var(--navy)"/>
      <path d="M270 0 Q254 226 118 342 L142 342 Q262 232 282 0 Z" fill="var(--teal)"/>
    </svg>

    <div class="brand brand--stacked">
      <span class="brand__dot"></span>
      <span class="brand__name">Hearthshine Crew</span>
    </div>

    <div class="contact">
      <h1 class="contact__name">Corin ter Haghe</h1>
      <p class="contact__title">Owner</p>
      <ul class="contact__list">
        <li class="contact__item">
          <svg viewBox="0 0 24 24"><path fill="var(--teal)" d="M6.6 10.8a15 15 0 0 0 6.6 6.6l2.2-2.2a1 1 0 0 1 1-.25 11.4 11.4 0 0 0 3.6.57 1 1 0 0 1 1 1V20a1 1 0 0 1-1 1A17 17 0 0 1 3 4a1 1 0 0 1 1-1h3.5a1 1 0 0 1 1 1c0 1.25.2 2.45.57 3.57a1 1 0 0 1-.25 1z"/></svg>
          1300 482 916
        </li>
        <li class="contact__item">
          <svg viewBox="0 0 24 24"><rect x="2" y="5" width="20" height="14" rx="2" fill="var(--teal)"/><path d="M3 6l9 7 9-7" fill="none" stroke="var(--navy)" stroke-width="2"/></svg>
          info@hearthshinecrew.com.au
        </li>
        <li class="contact__item">
          <svg viewBox="0 0 24 24"><circle cx="12" cy="12" r="10" fill="var(--teal)"/><path d="M2 12h20M12 2c3 3 3 17 0 20M12 2c-3 3-3 17 0 20" fill="none" stroke="var(--navy)" stroke-width="1.5"/></svg>
          www.hearthshinecrew.com.au
        </li>
      </ul>
    </div>
  </section>
</main>
</body>
</html>
```